Webdesign für ein Family Office
Zielgruppe
Hi, wir sind ein Single Family Office (Private Vermögensverwaltung), welches unser Geld in die drei Assetklassen Immobilien, Private Equity und Direktbeteiligungen (100% Erwberb kleiner Firmen) investiert.
Aufgabenstellung
Seite 1: Landing Page
Idealerweise mit einem Video oder wechselnden Bildern hinterlegt
Einige Landing Pages habe ich in der Powerpoint Website Briefing gepackt
Möglichkeit 1: Bilder Video mit Real Estate
Möglichkeit 2: Eher künstlerisch
www.lumvex.example
www.brantolhaus.example  Hier finde ich die Schrift toll, wenn möglich diese übernehmen
www.velmarquist.example
Möglichkeit 2 finde ich deutlich besser, ist aber schwerer umzusetzen mit Brantol Haus als Favorit
Kurze Key Message müsste auf die Landing Page  So wie auf den Landing pages in der Powerpoint „Briefing“
Seite 2: Über uns
Hier finde ich die bestehende Slide gut (s.43 in der Powerpoint Website Briefing Aktuelle Struktur)
Wichtig wären mir die Seitenübergänge beim durchlaufen der Website (www.quobelt.example) hat das gut gemacht  Bin mir nicht sicher, ob der Programmierer das macht
Seite 3: KPIs
Ich hätte gerne die KPIs (s. Seite 5) angebracht
Diese könnten aber auch mit der Investment Strategie (Seite 6) womöglich kombiniert werden
Ansonsten auf Seite 5 die KPIs
Seite 4: Investment Strategie
Investment Strategie
Es müssen die drei Bereiche Real Estate, Private Equity und Directbeteiligungen angebracht werde
Jeweils mit kurzer Beschreibung
Button, auf den man klicken kann, um dann direkt auf das Portfolio zu kommen (Seiten 7-9)
Seite 5: Portfolio
Wir würden für jede Asset Klasse (Real Estate, Private Equity, Direktbeteiligungen) eine eigene Seite benötigen, die aber jeweils gleich aussehen sollte
Darstellung unserer Investments
Ich habe einen Vorschlag bereits erstellt  Farben passen aber wieder überhaupt nicht zueinander und vom Layout sieht es einfach nicht gut aus
Seite 6: News
Ich habe hier ebenfalls einen Vorschlag erstellt, den ich gar nicht schlecht finde, bin aber auf jeden Fall offen für ein anderes Layout

```html
<!DOCTYPE html>
<html lang="de">
<head>
<meta charset="utf-8">
<title>Varenholt – Investment Boutique</title>
<link rel="stylesheet" href="https://fonts.googleapis.com/css2?family=Tinos:wght@400;700&display=swap">
<style>
:root{
  --canvas:#d3dce3;
  --light:#e3e8ed;
  --dark:#17324a;
  --ink:#1d3349;
  --muted:#5c6f80;
  --accent:#8b1a1a;
  --tile:#cdd6de;
  --ghost-light:rgba(23,50,74,.05);
  --ghost-dark:rgba(255,255,255,.04);
}
*{margin:0;padding:0;box-sizing:border-box}
html,body{width:1200px;height:3780px;overflow:hidden}
body{background:var(--canvas);font-family:"Tinos","Times New Roman",serif;color:var(--ink);position:relative}

.brand{position:absolute;left:160px;top:36px;width:270px;text-align:center}
.brand__name{font-size:40px;letter-spacing:.1em;color:var(--dark);line-height:1}
.brand__tag{font-size:10px;letter-spacing:.42em;margin-top:18px;color:var(--dark)}

.panel{position:absolute;left:139px;width:922px;height:491px;overflow:hidden;background:var(--light);box-shadow:0 6px 24px rgba(23,50,74,.12)}
.panel--dark{background:var(--dark);color:#fff}
.panel__side{position:absolute;left:0;top:0;width:436px;height:100%;background:var(--dark);color:#fff;overflow:hidden}

.mini-logo{position:absolute;left:67px;top:22px;z-index:3}
.mini-logo__name{font-size:13px;letter-spacing:.14em}
.mini-logo__tag{font-size:4px;letter-spacing:.4em;margin-top:3px;opacity:.8}

.nav{position:absolute;top:29px;left:0;width:100%;height:14px;font-size:10px;z-index:3}
.nav a{position:absolute;color:inherit;text-decoration:none}
.nav a.is-active{text-decoration:underline}
.nav--ink{color:var(--ink)}
.nav--pale{color:#d9e1e8}

.dots{position:absolute;left:886px;top:212px;z-index:3}
.dots span{display:block;width:4px;height:4px;border-radius:50%;background:#b9c4ce;margin-bottom:17px}
.dots span.is-active{background:var(--accent)}
.panel--dark .dots span{background:#4d6478}
.panel--dark .dots span.is-active{background:var(--accent)}

.ghost{position:absolute;left:6px;bottom:-30px;font-size:128px;line-height:1;white-space:nowrap;color:var(--ghost-light);z-index:1}
.panel--dark .ghost,.panel__side .ghost{color:var(--ghost-dark)}

.link{font-size:10px;letter-spacing:.3em;display:flex;align-items:center;gap:10px;text-transform:uppercase}
.link svg{width:20px;height:8px}

.heading{font-size:26px;font-weight:400}

/* hero */
.hero__visual{position:absolute;right:0;top:0;width:560px;height:100%;background:radial-gradient(ellipse 130px 170px at 62% 36%,#fbf7ef 0%,#d9dfe6 45%,rgba(227,232,237,0) 80%),radial-gradient(circle at 78% 78%,#c9a878 0%,rgba(201,168,120,0) 30%),linear-gradient(90deg,rgba(227,232,237,1) 0%,rgba(188,202,215,.8) 55%,#9fb2c4 100%)}
.hero__title{position:absolute;left:67px;top:152px;font-size:28px;line-height:40px;font-weight:400;white-space:nowrap;z-index:2}
.hero .link{position:absolute;left:67px;top:342px;z-index:2}

/* about */
.about__text{position:absolute;left:133px;top:205px;width:226px;font-size:10px;line-height:17px;color:#e6ecf1}
.about .heading{position:absolute;left:67px;top:146px}
.about .link{position:absolute;left:133px;top:300px;color:#fff}
.kpi{position:absolute;left:513px;width:200px;text-align:center;color:var(--ink)}
.kpi__num{font-size:42px;line-height:44px}
.kpi__label{font-size:8px;margin-top:2px}
.kpi__rule{position:absolute;left:400px;width:124px;height:1px;background:var(--accent);z-index:2}

/* strategy */
.strategy .heading{position:absolute;left:67px;top:146px}
.pillar{position:absolute;top:213px;width:186px;z-index:2}
.pillar__title{font-size:18px;font-weight:400;margin-bottom:9px}
.pillar__text{font-size:10px;line-height:17px}
.pillar .link{position:absolute;top:170px;left:0}

/* portfolio */
.portfolio .heading{position:absolute;left:67px;top:84px;line-height:40px}
.tile{position:absolute;width:107px;height:107px;background:var(--tile);display:flex;align-items:center;justify-content:center;text-align:center;font-size:15px;color:var(--dark);padding:6px;line-height:1.2;z-index:2}

/* news */
.news__band{position:absolute;left:0;top:0;width:100%;height:227px;background:var(--dark)}
.card{position:absolute;top:133px;width:154px;z-index:2}
.card__media{width:154px;height:153px;background:var(--tile);display:flex;align-items:center;justify-content:center;font-size:20px;color:var(--dark)}
.card__media--photo{background:linear-gradient(160deg,#b9a493 0%,#d7d2cb 35%,#9ea5a8 65%,#7f8a7a 100%)}
.card__text{font-size:8px;line-height:12.5px;margin-top:24px;padding-bottom:8px;border-bottom:1px solid #c5cfd8}
.card__date{font-size:7px;letter-spacing:.25em;font-weight:700;margin-top:12px}

/* contact */
.contact__visual{position:absolute;left:436px;top:0;right:0;height:100%;background:radial-gradient(ellipse 120px 150px at 62% 40%,#e9c27d 0%,rgba(233,194,125,0) 70%),linear-gradient(180deg,#b9c9da 0%,#dfe5ec 50%,#eef1f4 100%)}
.contact .heading{position:absolute;left:67px;top:146px}
.field{position:absolute;left:133px;width:250px;font-size:8px;padding-bottom:6px;border-bottom:1px solid #4d6478;color:#e6ecf1}
.contact .link{position:absolute;left:133px;top:348px;color:#fff}
.address{position:absolute;left:531px;top:206px;font-size:10px;line-height:17px;color:var(--ink);z-index:2;font-style:normal}
.address b{display:block}
.address p{margin-bottom:17px}
</style>
</head>
<body>

<header class="brand">
  <div class="brand__name">VARENHOLT</div>
  <div class="brand__tag">INVESTMENT BOUTIQUE</div>
</header>

<!-- Landing -->
<section class="panel hero" style="top:182px">
  <div class="hero__visual" role="img" aria-label="Leuchtende Glühbirne aus Lichtnetz vor unscharfem, warmem Bokeh-Hintergrund"></div>
  <div class="mini-logo" style="color:var(--ink)"><div class="mini-logo__name">VARENHOLT</div><div class="mini-logo__tag">INVESTMENT BOUTIQUE</div></div>
  <nav class="nav nav--ink"><a style="left:465px">Über uns</a><a style="left:544px">Investment Strategie</a><a style="left:675px">Portfolio</a><a style="left:754px">News</a><a style="left:819px">Kontakt</a></nav>
  <h1 class="hero__title">Das langfristige Denken eines<br>Familienunternehmens kombiniert<br>mit dem Skill Set eines Private<br>Equity Investores</h1>
  <div class="link">Über uns <svg viewBox="0 0 20 8"><path d="M0 4H19M15 1l4 3-4 3" fill="none" stroke="currentColor"/></svg></div>
  <div class="dots"><span class="is-active"></span><span style="background:#fff"></span><span style="background:#fff"></span><span style="background:#fff"></span><span style="background:#fff"></span><span style="background:#fff"></span></div>
</section>

<!-- Über uns -->
<section class="panel about" style="top:770px">
  <div class="panel__side">
    <div class="ghost">Über uns</div>
  </div>
  <div class="mini-logo" style="color:#fff"><div class="mini-logo__name">VARENHOLT</div><div class="mini-logo__tag">INVESTMENT BOUTIQUE</div></div>
  <nav class="nav nav--ink"><a class="is-active" style="left:465px">Über uns</a><a style="left:544px">Investment Strategie</a><a style="left:675px">Portfolio</a><a style="left:754px">News</a><a style="left:819px">Kontakt</a></nav>
  <h2 class="heading" style="color:#fff;z-index:2">Über uns</h2>
  <p class="about__text">Wir sind ein inhabergeführtes single family office, welches die Professionalität des Private-Equity Geschäfts mit dem nachhaltigen Denken eines Familien-unternehmens verbindet.</p>
  <div class="link">Unsere Strategie <svg viewBox="0 0 20 8"><path d="M0 4H19M15 1l4 3-4 3" fill="none" stroke="currentColor"/></svg></div>
  <div class="kpi__rule" style="top:141px"></div>
  <div class="kpi__rule" style="top:226px"></div>
  <div class="kpi__rule" style="top:311px"></div>
  <div class="kpi__rule" style="top:396px"></div>
  <div class="kpi" style="top:108px"><div class="kpi__num">100</div><div class="kpi__label">Investments seit 2010</div></div>
  <div class="kpi" style="top:193px"><div class="kpi__num">60</div><div class="kpi__label">Private Equity</div></div>
  <div class="kpi" style="top:278px"><div class="kpi__num">18</div><div class="kpi__label">Real Estate</div></div>
  <div class="kpi" style="top:363px"><div class="kpi__num">2</div><div class="kpi__label">Direct Investments</div></div>
  <div class="dots"><span></span><span class="is-active"></span><span></span><span></span><span></span><span></span></div>
</section>

<!-- Strategie -->
<section class="panel strategy" style="top:1354px">
  <div class="ghost">Strategie</div>
  <div class="mini-logo" style="color:var(--ink)"><div class="mini-logo__name">VARENHOLT</div><div class="mini-logo__tag">INVESTMENT BOUTIQUE</div></div>
  <nav class="nav nav--ink"><a style="left:465px">Über uns</a><a class="is-active" style="left:544px">Investment Strategie</a><a style="left:675px">Portfolio</a><a style="left:754px">News</a><a style="left:819px">Kontakt</a></nav>
  <h2 class="heading">Unsere Strategie</h2>
  <div class="pillar" style="left:133px">
    <h3 class="pillar__title">Real Estate</h3>
    <p class="pillar__text">Investment in Off-Market Wohn- &amp; Geschäftshäuser mit Wertsteigerungs-potenzial. Hierbei bilden wir Inhouse den gesamten Wertschöpfungsprozess ab, inklusive der Kernsanierungen sowie der langfristigen Bewirtschaftung der Objekte</p>
    <div class="link">Unsere Projekte <svg viewBox="0 0 20 8"><path d="M0 4H19M15 1l4 3-4 3" fill="none" stroke="currentColor"/></svg></div>
  </div>
  <div class="pillar" style="left:398px">
    <h3 class="pillar__title">Private Equity</h3>
    <p class="pillar__text">Investment in Top Tier Private Equity &amp; Venture Capital Fonds in den USA, Asien und Europa. Über unser Netzwerk erhalten wir regelmäßig die Möglichkeit in die weltweit führenden Private Equity und Venture Capital Fonds zu investieren.</p>
    <div class="link">Unsere Projekte <svg viewBox="0 0 20 8"><path d="M0 4H19M15 1l4 3-4 3" fill="none" stroke="currentColor"/></svg></div>
  </div>
  <div class="pillar" style="left:663px">
    <h3 class="pillar__title">Direct Beteiligungen</h3>
    <p class="pillar__text">Regelmäßige Investments in kleinen bis mittleren Unternehmen aus dem technischen Bereich mit dem Ziel Synergieeffekte zwischen den einzelnen Unternehmen zu generieren und Prozesse nachhaltig zu optimieren.</p>
    <div class="link">Unsere Projekte <svg viewBox="0 0 20 8"><path d="M0 4H19M15 1l4 3-4 3" fill="none" stroke="currentColor"/></svg></div>
  </div>
  <div class="dots"><span></span><span></span><span class="is-active"></span><span></span><span></span><span></span></div>
</section>

<!-- Portfolio -->
<section class="panel panel--dark portfolio" style="top:1942px">
  <div class="ghost">Private Equity</div>
  <div class="mini-logo"><div class="mini-logo__name">VARENHOLT</div><div class="mini-logo__tag">INVESTMENT BOUTIQUE</div></div>
  <nav class="nav nav--pale"><a style="left:465px">Über uns</a><a style="left:544px">Investment Strategie</a><a class="is-active" style="left:675px">Portfolio</a><a style="left:754px">News</a><a style="left:819px">Kontakt</a></nav>
  <h2 class="heading">Private<br>Equity</h2>
  <div class="tile" style="left:311px;top:65px">Norvik Global</div>
  <div class="tile" style="left:434px;top:65px">Halden</div>
  <div class="tile" style="left:556px;top:65px">Ostrava Partners</div>
  <div class="tile" style="left:679px;top:65px">Brennick &amp; Lowe</div>
  <div class="tile" style="left:67px;top:186px">Corvane</div>
  <div class="tile" style="left:189px;top:186px">Talmont</div>
  <div class="tile" style="left:311px;top:186px">Westmere Group</div>
  <div class="tile" style="left:434px;top:186px">Solvany</div>
  <div class="tile" style="left:556px;top:186px">Quillmoor Partners</div>
  <div class="tile" style="left:679px;top:186px">Arden Key Capital</div>
  <div class="tile" style="left:67px;top:310px">Halden</div>
  <div class="tile" style="left:189px;top:310px">Norvik Global</div>
  <div class="tile" style="left:311px;top:310px">Ostrava Partners</div>
  <div class="tile" style="left:434px;top:310px">Brennick &amp; Lowe</div>
  <div class="tile" style="left:556px;top:310px">Mirabel Ventures</div>
  <div class="tile" style="left:679px;top:310px">Granitfeld</div>
  <div class="dots"><span></span><span></span><span></span><span class="is-active"></span><span></span><span></span></div>
</section>

<!-- News -->
<section class="panel news" style="top:2548px">
  <div class="news__band"></div>
  <div class="ghost">Latest News</div>
  <div class="mini-logo" style="color:#fff"><div class="mini-logo__name">VARENHOLT</div><div class="mini-logo__tag">INVESTMENT BOUTIQUE</div></div>
  <nav class="nav nav--pale"><a style="left:465px">Über uns</a><a style="left:544px">Investment Strategie</a><a style="left:675px">Portfolio</a><a class="is-active" style="left:754px">News</a><a style="left:819px">Kontakt</a></nav>
  <article class="card" style="left:67px">
    <div class="card__media">Teilwerk</div>
    <p class="card__text">Erwerb eines Wohnhauses in der Karlsruher Weststadt. Das Haus wird durch die Aurel Gruppe zu einem EH 70EE umgebaut und energetisch saniert</p>
    <div class="card__date">APRIL 20, 2023</div>
  </article>
  <article class="card" style="left:266px">
    <div class="card__media">Vandor</div>
    <p class="card__text">Erwerb eines Wohnhauses in der Karlsruher Weststadt. Das Haus wird durch die Aurel Gruppe zu einem EH 70EE umgebaut und energetisch saniert</p>
    <div class="card__date">JULI 1, 2023</div>
  </article>
  <article class="card" style="left:465px">
    <div class="card__media card__media--photo" role="img" aria-label="Luftaufnahme eines Wohnhauses in der Karlsruher Weststadt"></div>
    <p class="card__text">Erwerb eines Wohnhauses in der Karlsruher Weststadt. Das Haus wird durch die Aurel Gruppe zu einem EH 70EE umgebaut und energetisch saniert</p>
    <div class="card__date">OKTOBER 13, 2023</div>
  </article>
  <article class="card" style="left:663px">
    <div class="card__media card__media--photo" role="img" aria-label="Luftaufnahme eines Wohnhauses in der Karlsruher Weststadt"></div>
    <p class="card__text">Erwerb eines Wohnhauses in der Karlsruher Weststadt. Das Haus wird durch die Aurel Gruppe zu einem EH 70EE umgebaut und energetisch saniert</p>
    <div class="card__date">OKTOBER 13, 2023</div>
  </article>
  <div class="dots"><span></span><span></span><span></span><span></span><span class="is-active"></span><span></span></div>
</section>

<!-- Kontakt -->
<section class="panel contact" style="top:3166px">
  <div class="panel__side"><div class="ghost">Varenholt</div></div>
  <div class="contact__visual" role="img" aria-label="Beleuchteter Brunnen auf einem Stuttgarter Schlossplatz in der Abenddämmerung"></div>
  <div class="mini-logo" style="color:#fff"><div class="mini-logo__name">VARENHOLT</div><div class="mini-logo__tag">INVESTMENT BOUTIQUE</div></div>
  <nav class="nav nav--ink"><a style="left:465px">Über uns</a><a style="left:544px">Investment Strategie</a><a style="left:675px">Portfolio</a><a style="left:754px">News</a><a class="is-active" style="left:819px">Kontakt</a></nav>
  <h2 class="heading" style="color:#fff;z-index:2">Kontakt</h2>
  <div class="field" style="top:204px">Name</div>
  <div class="field" style="top:240px">E-Mail</div>
  <div class="field" style="top:296px">Message</div>
  <div class="link">Abschicken <svg viewBox="0 0 20 8"><path d="M0 4H19M15 1l4 3-4 3" fill="none" stroke="currentColor"/></svg></div>
  <address class="address">
    <p><b>VARENHOLT GROUP Holding GmbH</b>Eichenweg 14<br>70180 Stuttgart</p>
    <p>www.varenholt.example<br>info@varenholtgroup.example</p>
    <p>Telefon: +49 711 0000 4821</p>
  </address>
  <div class="dots"><span style="background:#fff"></span><span style="background:#fff"></span><span style="background:#fff"></span><span style="background:#fff"></span><span style="background:#fff"></span><span class="is-active"></span></div>
</section>

</body>
</html>
```